Road Construction Company needs business cards

We would like a new business card designed for our business.

We're a road construction company based in Qld, Australia.

Can the business card please have the following information on it.

Name: Brent Malvoy
Position: General Manager
Phone: 0471 592 304
Email: Brent.malvoy@quendix.com.au
Address: 87 Harrowgate Ave, Pindarra, QLD, 4000
Website: www.quendix.com.au

Visually we'd like the card to be professional and simple.

Attached is our logo.

Our website is www.quendix.com.au

Target Market(s)

Men aged 25-60

Contact Information for Business Card

As listed in project description

Font styles to use
Serif

Requirements
Must have
• Large logo on back of card

```html
<!DOCTYPE html>
<html lang="en">
<head>
<meta charset="utf-8">
<title>Quendix Business Card</title>
<link rel="stylesheet" href="https://fonts.googleapis.com/css2?family=Tenor+Sans&display=swap">
<style>
  :root {
    --backdrop: #2a2b2d;
    --brand-blue: #2c9dd3;
    --brand-blue-deep: #2792c8;
    --navy: #0f4a9c;
    --accent: #3aa3dc;
    --ink: #3a3a3a;
    --paper: #ffffff;
    --paper-shade: #ececec;
    --rule: #9fc6e6;
  }
  * { margin: 0; padding: 0; box-sizing: border-box; }
  html, body {
    width: 1200px;
    height: 900px;
    overflow: hidden;
    background: var(--backdrop);
    font-family: "Tenor Sans", sans-serif;
  }
  .sheet {
    width: 1200px;
    height: 900px;
    display: flex;
    flex-direction: column;
    align-items: center;
    justify-content: center;
    gap: 40px;
  }
  .card {
    position: relative;
    width: 600px;
    height: 343px;
    border-radius: 34px;
    overflow: hidden;
    box-shadow: 0 14px 30px rgba(0,0,0,0.45);
  }
  .card-back {
    background: linear-gradient(100deg, var(--brand-blue-deep) 0%, var(--brand-blue) 45%, #35a6dc 100%);
  }
  .card-back .wordmark {
    position: absolute;
    left: 0; right: 0;
    top: 150px;
    text-align: center;
    color: var(--paper);
    font-size: 66px;
    letter-spacing: 4px;
  }
  .card-front {
    background: linear-gradient(110deg, var(--paper-shade) 0%, var(--paper) 55%, var(--paper) 100%);
  }
  .card-front .wordmark {
    position: absolute;
    left: 0; right: 0;
    top: 46px;
    text-align: center;
    color: var(--navy);
    font-size: 58px;
    letter-spacing: 4px;
  }
  .person {
    position: absolute;
    right: 330px;
    top: 168px;
    text-align: right;
  }
  .person .name {
    color: var(--navy);
    font-size: 19px;
    text-transform: uppercase;
    letter-spacing: 0.3px;
  }
  .person .role {
    color: var(--ink);
    font-size: 16px;
    margin-top: 2px;
  }
  .divider {
    position: absolute;
    left: 290px;
    top: 140px;
    width: 1px;
    height: 90px;
    background: var(--rule);
  }
  .contacts {
    position: absolute;
    left: 306px;
    top: 146px;
    list-style: none;
  }
  .contacts li {
    display: flex;
    align-items: center;
    gap: 8px;
    color: var(--ink);
    font-size: 14.5px;
    height: 26px;
  }
  .contacts svg { width: 14px; height: 14px; flex: none; }
  .address {
    position: absolute;
    left: 0; right: 0;
    top: 284px;
    padding-left: 90px;
    text-align: center;
    color: var(--ink);
    font-size: 15px;
  }
</style>
</head>
<body>
<main class="sheet">
  <section class="card card-back" aria-label="Card back">
    <div class="wordmark">QUENDIX</div>
  </section>

  <section class="card card-front" aria-label="Card front">
    <div class="wordmark">QUENDIX</div>

    <div class="person">
      <p class="name">Brent Malvoy</p>
      <p class="role">General Manager</p>
    </div>

    <div class="divider"></div>

    <ul class="contacts">
      <li>
        <svg viewBox="0 0 16 16" aria-hidden="true"><path fill="var(--accent)" d="M3.6 1.2l2.3 2.6-1.2 1.7c.9 2 2.3 3.5 4.3 4.4l1.7-1.2 2.6 2.3-1.4 2.4C7 13.2 2.7 8.9 1.2 2.6z"/></svg>
        0471 592 304
      </li>
      <li>
        <svg viewBox="0 0 16 16" aria-hidden="true"><g fill="none" stroke="var(--accent)" stroke-width="1.4"><circle cx="8" cy="8" r="6.3"/><ellipse cx="8" cy="8" rx="2.8" ry="6.3"/><path d="M1.8 8h12.4"/></g></svg>
        www.quendix.com.au
      </li>
      <li>
        <svg viewBox="0 0 16 16" aria-hidden="true"><rect x="1.5" y="3.5" width="13" height="9.5" rx="1" fill="var(--accent)"/><path d="M1.8 4l6.2 5 6.2-5" fill="none" stroke="#fff" stroke-width="1.2"/></svg>
        Brent.malvoy@quendix.com.au
      </li>
    </ul>

    <p class="address">87 Harrowgate Ave, Pindarra, QLD, 4000</p>
  </section>
</main>
</body>
</html>
```